Redesign My Travel Agency Agreements

I need my reservation request forms redesigned into a professional contract. This is a travel agency contract. Just needs to look professional. PDF format please. See attached
Target Market(s)
travel agencies and travelers
Industry/Entity Type
Travel Agency
Font styles to use
Other font styles liked:
- open
Requirements
Must have
- I need my reservation request forms redesigned into a professional contract. This is a travel agency contract. Just needs to look professional. PDF format please. See attached
Nice to have
Should not have

```html
<!DOCTYPE html>
<html lang="en">
<head>
<meta charset="utf-8">
<title>Booking Confirmation</title>
<link href="https://fonts.googleapis.com/css2?family=Inter:wght@400;500;700&family=Roboto+Condensed:wght@700&display=swap" rel="stylesheet">
<style>
  :root {
    --brand-blue: #005b8e;
    --ink: #231f20;
    --muted: #6d6e71;
    --paper: #ffffff;
  }
  * { margin: 0; padding: 0; box-sizing: border-box; }
  html, body { width: 927px; height: 1200px; overflow: hidden; background: var(--paper); }
  body { position: relative; font-family: "Inter", Arial, sans-serif; color: var(--ink); }

  .masthead {
    position: absolute; left: 0; top: 0; width: 927px; height: 162px;
    background: var(--brand-blue); color: var(--paper);
  }
  .brand {
    position: absolute; left: 52px; top: 60px;
    font-weight: 700; font-size: 22px; letter-spacing: 0.5px; line-height: 1.25;
    text-transform: uppercase;
  }
  .brand small { display: block; font-size: 14px; letter-spacing: 1px; }
  .sender-address {
    position: absolute; right: 52px; top: 48px; text-align: right;
    font-weight: 700; font-size: 15px; line-height: 18px; font-style: normal;
  }

  .doc-title {
    position: absolute; left: 50px; top: 186px;
    font-size: 56px; font-weight: 400; letter-spacing: -0.5px; line-height: 1.2;
  }
  .doc-title strong { font-weight: 700; }

  .booking-details {
    position: absolute; left: 52px; top: 281px; width: 823px;
    border-collapse: collapse; border: 3px solid var(--ink);
  }
  .booking-details td {
    height: 49px; border-top: 1px solid var(--ink); border-left: 1px solid var(--ink);
    padding: 0 8px 0 8px; vertical-align: middle;
    font-family: "Roboto Condensed", "Arial Narrow", sans-serif; font-weight: 700; font-size: 15px;
  }
  .booking-details tr:first-child td { border-top: none; }
  .booking-details td:first-child { border-left: none; }
  .col-a { width: 316px; }
  .col-b { width: 281px; }

  .terms { position: absolute; left: 52px; top: 668px; width: 826px; }
  .terms h2 { font-size: 23px; font-weight: 700; line-height: 30px; }
  .terms h3 { font-size: 18.5px; font-weight: 700; color: var(--muted); line-height: 24px; margin-top: 4px; margin-bottom: 4px; }
  .terms p { font-size: 13.4px; line-height: 16.4px; margin-bottom: 16px; }
  .terms p.spaced { margin-bottom: 17px; }
</style>
</head>
<body>
  <header class="masthead">
    <div class="brand">Waypoint Travel Rewards<small>Booking Services</small></div>
    <address class="sender-address">
      Waypoint Travel Rewards<br>
      48 Harbor Lane<br>
      Suite 310<br>
      Portland, ME 04101
    </address>
  </header>

  <h1 class="doc-title"><strong>Booking</strong> Confirmation</h1>

  <table class="booking-details">
    <tr><td colspan="3">Date:</td></tr>
    <tr><td colspan="3">Hotel Name:</td></tr>
    <tr><td colspan="3">Hotel Address:</td></tr>
    <tr><td class="col-a">City:</td><td class="col-b">State:</td><td>Zip:</td></tr>
    <tr><td colspan="3">Hotel Confirmation/Reservation #:</td></tr>
    <tr><td colspan="3">Primary Guest:</td></tr>
    <tr><td class="col-a">Check-In Date:</td><td colspan="2">Check-Out Date:</td></tr>
  </table>

  <section class="terms">
    <h2>TERMS AND CONDITIONS</h2>
    <h3>CONFIRMATION</h3>
    <p><strong>ALL BOOKINGS ARE FINAL</strong> and cannot be canceled, refunded, changed, exchanged or transferred. When we book your accommodations we will contact you by email. Reservation is guaranteed for arrival on the confirmed check-in date only. If you do not check-in on the first day of your reservation and you do not alert the hotel in advance, the remaining portion of your reservation will be canceled and you will not be entitled to a refund.</p>
    <h3>CANCELLATION</h3>
    <p><strong>ALL BOOKINGS ARE FINAL</strong> and cannot be canceled, refunded, changed, exchanged or transferred. If you cancel after your reservation is booked you will forfeit your room deposit plus any other fees you paid for the room.</p>
    <h3>TRAVEL DOCUMENTS</h3>
    <p class="spaced">You will need a valid photo ID to check in to your hotel. Hotels require a credit card imprint or a cash deposit to guarantee incidental charges (phone calls, room service, parking, resort fees, energy charges, etc.) that you may incur while staying at the property. The credit amount will vary by hotel. Should you have a special request, please contact your property directly at the number listed above to coordinate your arrangements. You may incur additional fees for special arrangements if applicable. If you are going out of the country you are required to bring your Passport/Visa, no exceptions.</p>
    <p>Additional Disclosures: Some hotels/resorts may apply additional charges that are not included in your reservation such as parking, convention or resort fees. You will be required to pay any such fees directly to the hotel (usually upon check-in). Once we book your reservation, we recommend contacting your hotel to ask about any additional charges. If you need to extend your stay beyond the dates you booked, please contact the hotel directly. We cannot guarantee the rate for any additional days. If you have any questions please contact the hotel listed above or go back to our website and submit a “Need Help” Ticket.</p>
  </section>
</body>
</html>
```